Front & Back Book Cover Design

Title:
THE QUIET LANDLORD: How to Grow Comfort and Capital Through Property You Merely Guide
Author:
Wes T. Marlund
Design Philosophy:
A modern, minimalist-luxury aesthetic that feels visionary and intelligent — positioned between business innovation (The Nimble Venture), modern finance (The Temperament of Wealth), and timeless real estate insight (Bold Uncle Meek Uncle).
Think: clean, bold, and idea-driven — a visual reflection of the book’s central concept: wealth through clarity, not clutter.
Back Cover:
To include book description along with author photo and bio
Files:
PNG, PDF, EPUB

```html
<!DOCTYPE html>
<html lang="en">
<head>
<meta charset="utf-8">
<title>The Quiet Landlord — Wes T. Marlund</title>
<link rel="stylesheet" href="https://fonts.googleapis.com/css2?family=Archivo:wght@400;700&family=Montserrat:wght@500&family=Work+Sans:wght@400&display=swap">
<style>
  :root {
    --cover-black: #000000;
    --gold: #c29f4f;
    --silver: #bbbcbe;
    --white: #ffffff;
  }
  html, body {
    margin: 0;
    padding: 0;
    width: 800px;
    height: 1200px;
    overflow: hidden;
    background: var(--cover-black);
  }
  .cover {
    position: relative;
    width: 800px;
    height: 1200px;
    background: var(--cover-black);
    overflow: hidden;
  }
  .title {
    margin: 0;
    font-weight: 700;
  }
  .title-line {
    position: absolute;
    left: 0;
    width: 800px;
    text-align: center;
    font-family: "Archivo", Arial, sans-serif;
    line-height: 1;
    white-space: nowrap;
  }
  .title-article {
    top: 58px;
    font-size: 90px;
    font-weight: 400;
    color: var(--gold);
  }
  .title-main {
    top: 140px;
    font-size: 138px;
    font-weight: 700;
    color: var(--silver);
  }
  .title-accent {
    top: 265px;
    font-size: 128px;
    font-weight: 700;
    color: var(--gold);
    letter-spacing: -0.01em;
  }
  .subtitle {
    position: absolute;
    top: 430px;
    left: 0;
    width: 800px;
    margin: 0;
    text-align: center;
    font-family: "Work Sans", Arial, sans-serif;
    font-weight: 400;
    font-size: 44px;
    line-height: 70px;
    letter-spacing: 0.06em;
    color: var(--white);
  }
  .emblem {
    position: absolute;
    left: 281px;
    top: 787px;
    width: 281px;
    height: 193px;
    background: linear-gradient(160deg, rgba(194,159,79,0.28), rgba(194,159,79,0.08));
  }
  .author {
    position: absolute;
    top: 1080px;
    left: 0;
    width: 800px;
    margin: 0;
    text-align: center;
    font-family: "Montserrat", Arial, sans-serif;
    font-weight: 500;
    font-size: 58px;
    line-height: 1;
    letter-spacing: 0.1em;
    color: var(--gold);
    white-space: nowrap;
  }
</style>
</head>
<body>
  <main class="cover">
    <h1 class="title">
      <span class="title-line title-article">THE</span>
      <span class="title-line title-main">QUIET</span>
      <span class="title-line title-accent">LANDLORD</span>
    </h1>
    <p class="subtitle">How to Grow Comfort and<br>Capital Through Property<br>You Merely Guide</p>
    <div class="emblem" role="img" aria-label="Gold line drawing of stepped modern buildings on a ground line"></div>
    <p class="author">WES T. MARLUND</p>
  </main>
</body>
</html>
```